Moulding supply company needs a Door Hanger Design

Door Hanger Design Request from Ledge Craft
www. ledgecrafts.example
We are moulding factory outlet in Toronto. Provide high quality moulding materials with competitive price like crown mouldings, casings, wainscoting, flatstocks, baseboards. We also provide professional installation for our clients. This door hanger will help the home owner easily find a local factory supplier with providing the materials as well as installation.

Detail request for design:
Size: 4”x11”, vertical
Shape: Rectangle

Content:
Front
1. Logo, see attachment(Use the left one, horizontal one)
2. Moulding factory outlet direct sale
3. Supply high quality Crown mouldings, baseboards, casings and wainscotings with competitive price
4. Installation & delivery
#2 content is the most important content, should be bold and readable
#3 can be smaller font compare to #2

Address: 47 North Willow Vale Rd, Richmond Hill, ON L4B 3K9
Telephone: 416 555 0143
416 555 0187
Email: info@ledgecrafts.example

Back
Slogan: Convert plain room into designer’s interiors

Telephone: 416 555 0143
416 555 0187
Email: info@ledgecrafts.example

Images:
Front
1. Display our productions for crown mouldings, baseboards, casings and wainscotings, refer to our website www.ledgecrafts.example. (The winner finally we will provide the high resolution images, low resolution please copy from our website so far)
Back
2. Display 4-6 nice images for 1. wainscoting walls 2. feature walls, 3. waffle ceiling like attached below. BUT PLEASE DON'T USE THE IMAGES PROVIDED, THIS IS ONLY A SAMPLE. Please use high resolution images for printing. ALSO PLEASE DON'T LIMIT YOUR CREATIVITY TO USE 4 SQUARES LIKE BELOW IMAGES. Please provide more ideas

Note:
1. Please do the bleeding for final printing production
2. Images have to be high resolution for ready to print
3. Style need to be fresh, clean, easy to read, modern and magazine style
4. Information has to be readable, easy to find, front and back both need to display company address, telephone, email, you can use icon or abbreviation to do these information.

Thanks,
Ledge Crafts

```html
<!DOCTYPE html>
<html lang="en">
<head>
<meta charset="utf-8">
<title>Ledge Crafts — Door Hangers</title>
<link rel="stylesheet" href="https://fonts.googleapis.com/css2?family=Montserrat:wght@400;500;700;800&family=Oswald:wght@300;500;600&display=swap">
<style>
  :root{
    --stage:#7a7979;
    --orange:#f05a28;
    --blue:#2150a3;
    --slate:#5d6670;
    --white:#ffffff;
    --ink:#111111;
  }
  *{box-sizing:border-box;margin:0;padding:0}
  html,body{width:1200px;height:1200px;overflow:hidden;background:var(--stage)}
  .hanger{position:absolute;top:70px;width:392px;height:1037px;box-shadow:4px 6px 10px rgba(0,0,0,.35);overflow:hidden}
  .hanger--front{left:155px}
  .hanger--back{left:614px}
  .hanger__art{position:absolute;inset:0;width:392px;height:1037px;display:block}
  .layer{position:absolute;left:0;width:100%}

  .brand{position:absolute;display:flex;align-items:center}
  .brand__mark{width:30px;height:30px;background:var(--orange);flex:none}
  .brand__name{font-family:"Montserrat",sans-serif;font-weight:500;color:var(--slate);letter-spacing:1.5px;white-space:nowrap}
  .brand__tag{font-family:"Montserrat",sans-serif;font-weight:400;color:var(--slate);letter-spacing:2.6px;white-space:nowrap;position:absolute}

  .front-brand{left:30px;top:388px;gap:12px}
  .front-brand .brand__name{font-size:31px}
  .front-tag{left:109px;top:432px;font-size:11px}

  .direct-sale{position:absolute;left:34px;top:457px;width:326px;height:53px;background:var(--blue);border-radius:27px;
    color:var(--white);font-family:"Montserrat",sans-serif;font-weight:800;font-size:17.5px;line-height:20px;text-align:center;
    display:flex;flex-direction:column;justify-content:center;letter-spacing:.4px}

  .supply-box{position:absolute;left:22px;top:803px;width:346px;height:101px;border:1.5px solid var(--blue);border-radius:10px;
    background:var(--white);text-align:center;font-family:"Oswald",sans-serif;text-transform:uppercase;padding-top:4px}
  .supply-box__lead{font-weight:500;font-size:18px;line-height:21px;color:var(--ink)}
  .supply-box__items{font-weight:500;font-size:22px;line-height:23px;color:var(--orange)}
  .supply-box__note{font-weight:500;font-size:17px;line-height:21px;color:var(--blue)}

  .address-bar{top:915px;height:30px;background:var(--blue);color:var(--white);font-family:"Oswald",sans-serif;font-weight:300;
    font-size:15.5px;line-height:30px;text-align:center;text-transform:uppercase;white-space:nowrap}
  .contact-bar{top:945px;height:92px;background:var(--orange);color:var(--white);font-family:"Montserrat",sans-serif;font-weight:700;text-align:center}
  .contact-bar__icons{display:flex;justify-content:center;gap:13px;padding-top:3px}
  .contact-bar__icons svg{width:26px;height:26px;display:block}
  .contact-bar__phones{font-size:17px;line-height:20px;margin-top:3px}
  .contact-bar__email{font-size:15.5px;line-height:19px}

  .back-brand{left:0;width:100%;top:520px;flex-direction:column;gap:10px}
  .back-brand .brand__mark{width:26px;height:26px}
  .back-brand .brand__name{font-size:28px}
  .back-tag{left:0;width:100%;text-align:center;top:604px;font-size:8px}

  .slogan{position:absolute;left:78px;top:648px;width:236px;height:53px;background:var(--orange);text-align:center;
    font-family:"Oswald",sans-serif;font-weight:600;text-transform:uppercase;padding-top:2px}
  .slogan__top{color:var(--ink);font-size:18px;line-height:22px}
  .slogan__bottom{color:var(--white);font-size:22px;line-height:25px}
</style>
</head>
<body>

<!-- Front -->
<section class="hanger hanger--front">
  <svg class="hanger__art" viewBox="0 0 392 1037">
    <defs>
      <linearGradient id="frontTopTone" x1="0" y1="0" x2="0" y2="1">
        <stop offset="0" stop-color="#4d4643"/>
        <stop offset=".45" stop-color="#6c6663"/>
        <stop offset="1" stop-color="#d2d2d2"/>
      </linearGradient>
      <linearGradient id="frontCrownTone" x1="0" y1="0" x2="1" y2="1">
        <stop offset="0" stop-color="#a8a6a4"/>
        <stop offset=".5" stop-color="#76716d"/>
        <stop offset="1" stop-color="#5c5855"/>
      </linearGradient>
    </defs>
    <rect x="0" y="0" width="392" height="620" fill="url(#frontTopTone)" role="img" aria-label="Photo of a dark panelled wainscoting feature wall with a white vase"/>
    <path d="M0,532 Q196,455 392,540 L392,1037 L0,1037 Z" fill="var(--white)"/>
    <path d="M0,545 Q196,474 392,552 L392,712 Q200,872 0,724 Z" fill="url(#frontCrownTone)" role="img" aria-label="Photo of white crown moulding at a ceiling corner"/>
    <path d="M0,724 Q200,872 392,712 L392,730 Q200,890 0,732 Z" fill="var(--orange)"/>
    <circle cx="196" cy="172" r="77" fill="var(--stage)"/>
  </svg>

  <div class="brand front-brand"><span class="brand__mark"></span><span class="brand__name">LEDGE CRAFTS</span></div>
  <div class="brand__tag front-tag">FOR ALL TYPES OF PROJECTS</div>

  <div class="direct-sale"><span>MOULDING FACTORY OUTLET</span><span>DIRECT SALE</span></div>

  <div class="supply-box">
    <div class="supply-box__lead">Supply high quality</div>
    <div class="supply-box__items">Crown mouldings, baseboards,<br>casings and wainscotings</div>
    <div class="supply-box__note">with competitive price</div>
  </div>

  <div class="layer address-bar">47 North Willow Vale Rd, Richmond Hill, ON L4B 3K9</div>
  <div class="layer contact-bar">
    <div class="contact-bar__icons">
      <svg viewBox="0 0 26 26" aria-label="Email"><circle cx="13" cy="13" r="12" fill="var(--white)"/><circle cx="13" cy="13" r="10" fill="var(--orange)"/><rect x="7" y="9" width="12" height="8.5" fill="none" stroke="var(--white)" stroke-width="1.4"/><path d="M7,9 L13,14 L19,9" fill="none" stroke="var(--white)" stroke-width="1.4"/></svg>
      <svg viewBox="0 0 26 26" aria-label="Phone"><circle cx="13" cy="13" r="12" fill="var(--white)"/><circle cx="13" cy="13" r="10" fill="var(--orange)"/><path d="M9.2,7.5 L11.3,7.2 L12.2,10.2 L10.8,11.3 Q12,14 14.7,15.2 L15.8,13.8 L18.8,14.7 L18.5,16.8 Q17.5,18.6 15,18 Q9,16 8,11 Q7.6,8.6 9.2,7.5 Z" fill="var(--white)"/></svg>
    </div>
    <div class="contact-bar__phones">416 555 0143 / 416 555 0187</div>
    <div class="contact-bar__email">info@ledgecrafts.example</div>
  </div>
</section>

<!-- Back -->
<section class="hanger hanger--back">
  <svg class="hanger__art" viewBox="0 0 392 1037">
    <defs>
      <linearGradient id="backTopTone" x1="0" y1="0" x2="0" y2="1">
        <stop offset="0" stop-color="#cfcfcc"/>
        <stop offset="1" stop-color="#b3b2ae"/>
      </linearGradient>
      <linearGradient id="backWallTone" x1="0" y1="0" x2="1" y2="0">
        <stop offset="0" stop-color="#3e3e40"/>
        <stop offset=".7" stop-color="#4d4d4f"/>
        <stop offset="1" stop-color="#c9c9c7"/>
      </linearGradient>
      <linearGradient id="backCeilingTone" x1="0" y1="0" x2="0" y2="1">
        <stop offset="0" stop-color="#d8d4cd"/>
        <stop offset=".55" stop-color="#c9b8a8"/>
        <stop offset="1" stop-color="#c0977e"/>
      </linearGradient>
    </defs>
    <rect x="0" y="0" width="392" height="320" fill="url(#backTopTone)" role="img" aria-label="Photo of a grey hallway with wainscoting panels and wall sconces"/>
    <rect x="0" y="600" width="392" height="320" fill="url(#backCeilingTone)" role="img" aria-label="Photo of a white waffle ceiling above a room with a chandelier"/>
    <path d="M0,228 Q200,190 392,290 L392,560 L0,560 Z" fill="var(--white)"/>
    <path d="M0,242 Q200,212 392,368 L392,470 Q220,380 0,490 Z" fill="url(#backWallTone)" role="img" aria-label="Photo of a living room with a dark damask feature wall, television and sofa"/>
    <path d="M0,478 Q215,370 392,458 L392,560 L0,560 Z" fill="var(--orange)"/>
    <path d="M0,492 Q215,385 392,480 L392,560 L0,560 Z" fill="var(--blue)"/>
    <path d="M0,508 Q215,400 392,470 L392,668 C300,740 200,790 0,735 Z" fill="var(--white)"/>
    <circle cx="196" cy="172" r="77" fill="var(--stage)"/>
  </svg>

  <div class="brand back-brand"><span class="brand__mark"></span><span class="brand__name">LEDGE CRAFTS</span></div>
  <div class="brand__tag back-tag">FOR ALL TYPES OF PROJECTS</div>

  <div class="slogan">
    <div class="slogan__top">Convert plain room into</div>
    <div class="slogan__bottom">Designer’s interiors</div>
  </div>

  <div class="layer address-bar">47 North Willow Vale Rd, Richmond Hill, ON L4B 3K9</div>
  <div class="layer contact-bar">
    <div class="contact-bar__icons">
      <svg viewBox="0 0 26 26" aria-label="Email"><circle cx="13" cy="13" r="12" fill="var(--white)"/><circle cx="13" cy="13" r="10" fill="var(--orange)"/><rect x="7" y="9" width="12" height="8.5" fill="none" stroke="var(--white)" stroke-width="1.4"/><path d="M7,9 L13,14 L19,9" fill="none" stroke="var(--white)" stroke-width="1.4"/></svg>
      <svg viewBox="0 0 26 26" aria-label="Phone"><circle cx="13" cy="13" r="12" fill="var(--white)"/><circle cx="13" cy="13" r="10" fill="var(--orange)"/><path d="M9.2,7.5 L11.3,7.2 L12.2,10.2 L10.8,11.3 Q12,14 14.7,15.2 L15.8,13.8 L18.8,14.7 L18.5,16.8 Q17.5,18.6 15,18 Q9,16 8,11 Q7.6,8.6 9.2,7.5 Z" fill="var(--white)"/></svg>
    </div>
    <div class="contact-bar__phones">416 555 0143 / 416 555 0187</div>
    <div class="contact-bar__email">info@ledgecrafts.example</div>
  </div>
</section>

</body>
</html>
```